For lease banners for Businesses

I need to turn all of these banners into high quality graphics so I can get them printed on vinyl vertical banners that are 44"W x 88"H. So I need them most likely to be vector artwork, and ready to upload to a custom vinyl print shop.

```html
<!DOCTYPE html>
<html lang="en">
<head>
<meta charset="utf-8">
<title>Halvern Estates – Now Leasing</title>
<link rel="stylesheet" href="https://fonts.googleapis.com/css2?family=Bebas+Neue&family=Oswald:wght@400;500&family=Poppins:wght@400;600&display=swap">
<style>
  :root {
    --ink: #000000;
    --paper: #ffffff;
    --gold: #b87f00;
    --rule: #5a4a20;
    --headline: "Bebas Neue", "Oswald", sans-serif;
    --label: "Oswald", sans-serif;
    --body: "Poppins", sans-serif;
  }
  * { margin: 0; padding: 0; box-sizing: border-box; }
  html, body { width: 1200px; height: 2400px; overflow: hidden; background: var(--ink); }
  .banner { position: relative; width: 1200px; height: 2400px; background: var(--ink); color: var(--paper); overflow: hidden; }
  .abs { position: absolute; }

  .street-photo {
    left: 560px; top: 0; width: 640px; height: 1260px;
    background:
      linear-gradient(180deg, rgba(0,0,0,0) 55%, #000 100%),
      linear-gradient(90deg, #000 0%, rgba(0,0,0,0) 40%),
      linear-gradient(160deg, #1a1a1a 0%, #5e5e5e 30%, #3a3a3a 55%, #151515 75%, #000 100%);
  }

  .brand-dot { border-radius: 50%; background: var(--gold); }
  .brand-name { font-family: var(--body); font-weight: 600; color: var(--paper); white-space: nowrap; }
  .brand-top-dot { left: 570px; top: 170px; width: 60px; height: 60px; }
  .brand-top-name { left: 300px; top: 262px; width: 600px; text-align: center; font-size: 60px; line-height: 72px; }

  .headline { left: 110px; font-family: var(--headline); line-height: 1; color: var(--paper); white-space: nowrap; transform-origin: left top; }
  .headline-1 { top: 458px; font-size: 147px; transform: scaleX(1.1); }
  .headline-2 { top: 579px; font-size: 222px; color: var(--gold); }
  .headline-3 { top: 759px; font-size: 160px; }
  .headline-4 { top: 893px; font-size: 160px; }

  .uses { left: 110px; top: 1068px; width: 563px; display: flex; justify-content: space-between; align-items: center; font-family: var(--headline); font-size: 42px; letter-spacing: 2px; line-height: 42px; }
  .uses .dot { width: 10px; height: 10px; border-radius: 50%; background: var(--gold); }
  .uses-rule { left: 110px; top: 1132px; width: 563px; height: 2px; background: var(--rule); }
  .intro { left: 110px; top: 1143px; font-family: var(--body); font-size: 37px; line-height: 50px; }

  .features { left: 110px; top: 1280px; width: 980px; list-style: none; }
  .feature { position: relative; height: 131px; border-bottom: 1px solid var(--rule); }
  .feature:last-child { border-bottom: none; }
  .feature-icon { position: absolute; left: 8px; top: 16px; width: 90px; height: 86px; }
  .feature-title { position: absolute; left: 119px; top: 14px; font-family: var(--headline); font-weight: 400; font-size: 44px; letter-spacing: 2px; line-height: 44px; }
  .feature-text { position: absolute; left: 119px; top: 64px; font-family: var(--body); font-size: 27px; line-height: 36px; white-space: nowrap; }

  .leasing-band { left: 0; top: 1948px; width: 1200px; height: 172px; background: var(--gold); }
  .phone-badge { left: 110px; top: 1984px; width: 100px; height: 100px; border-radius: 50%; background: #0d0b08; }
  .now-leasing { left: 242px; top: 1990px; font-family: var(--label); font-weight: 500; font-size: 78px; line-height: 90px; transform: scaleX(0.82); transform-origin: left; white-space: nowrap; color: var(--ink); }
  .band-divider { left: 599px; top: 1971px; width: 2px; height: 126px; background: rgba(0,0,0,0.35); }
  .contact { left: 644px; top: 1950px; font-family: var(--label); color: var(--ink); transform: scaleX(0.82); transform-origin: left; white-space: nowrap; }
  .contact-label { font-size: 44px; font-weight: 400; line-height: 56px; }
  .contact-phone { font-size: 44px; font-weight: 500; line-height: 56px; }
  .contact-email { font-size: 44px; font-weight: 400; line-height: 56px; }

  .brand-foot-dot { left: 352px; top: 2200px; width: 50px; height: 50px; }
  .brand-foot-name { left: 424px; top: 2189px; font-size: 56px; line-height: 72px; }
</style>
</head>
<body>
<main class="banner">
  <div class="abs street-photo" role="img" aria-label="Black-and-white photo of a downtown street lined with brick and glass buildings"></div>

  <div class="abs brand-dot brand-top-dot"></div>
  <div class="abs brand-name brand-top-name">Halvern Estates</div>

  <h1>
    <span class="abs headline headline-1">SOMETHING</span>
    <span class="abs headline headline-2">GREAT</span>
    <span class="abs headline headline-3">BELONGS</span>
    <span class="abs headline headline-4">HERE.</span>
  </h1>

  <div class="abs uses"><span>RETAIL</span><span class="dot"></span><span>RESTAURANT</span><span class="dot"></span><span>OFFICE</span></div>
  <div class="abs uses-rule"></div>
  <p class="abs intro">Be part of Downtown Larkfield's<br>fastest-growing destination.</p>

  <ul class="abs features">
    <li class="feature">
      <svg class="feature-icon" viewBox="0 0 90 86" fill="none" stroke="#b87f00" stroke-width="2.5">
        <path d="M45 82 C30 62 16 48 16 32 A29 29 0 0 1 74 32 C74 48 60 62 45 82 Z"/>
        <circle cx="45" cy="31" r="12"/>
      </svg>
      <h2 class="feature-title">HIGH VISIBILITY</h2>
      <p class="feature-text">Prime location with strong street exposure.</p>
    </li>
    <li class="feature">
      <svg class="feature-icon" viewBox="0 0 90 86" fill="none" stroke="#b87f00" stroke-width="2.5">
        <circle cx="30" cy="26" r="8"/><circle cx="60" cy="26" r="8"/>
        <circle cx="18" cy="46" r="8"/><circle cx="45" cy="46" r="8"/><circle cx="72" cy="46" r="8"/>
        <path d="M4 72 C4 58 32 58 32 72 Z M31 72 C31 58 59 58 59 72 Z M58 72 C58 58 86 58 86 72 Z"/>
      </svg>
      <h2 class="feature-title">DOWNTOWN TRAFFIC</h2>
      <p class="feature-text">Surrounded by thriving businesses, events and foot traffic.</p>
    </li>
    <li class="feature">
      <svg class="feature-icon" viewBox="0 0 90 86" fill="none" stroke="#b87f00" stroke-width="2.5">
        <rect x="8" y="4" width="74" height="78"/>
        <path d="M14 10 H76 V76 H58 V58 H14 Z"/>
        <rect x="20" y="16" width="16" height="14"/><rect x="42" y="16" width="12" height="14"/>
        <rect x="20" y="38" width="20" height="12"/><path d="M60 20 V40 H70"/>
      </svg>
      <h2 class="feature-title">FLEXIBLE FLOORPLANS</h2>
      <p class="feature-text">Customizable layouts to fit your business needs.</p>
    </li>
    <li class="feature">
      <svg class="feature-icon" viewBox="0 0 90 86" fill="none" stroke="#b87f00" stroke-width="2.5">
        <circle cx="45" cy="24" r="16"/>
        <path d="M37 24 L43 30 L54 18"/>
        <rect x="4" y="44" width="12" height="30"/><rect x="74" y="44" width="12" height="30"/>
        <path d="M16 50 H30 L45 62 L58 50 H74 M16 68 L40 80 L62 68 H74"/>
      </svg>
      <h2 class="feature-title">LOCAL OWNERSHIP</h2>
      <p class="feature-text">Proudly owned and invested in downtown.</p>
    </li>
    <li class="feature">
      <svg class="feature-icon" viewBox="0 0 90 86" fill="none" stroke="#b87f00" stroke-width="2.5">
        <path d="M14 8 L22 4 L78 64 L72 72 Z"/>
        <path d="M66 66 L80 78"/>
        <circle cx="20" cy="70" r="10"/>
        <path d="M27 63 L62 26"/>
        <path d="M58 18 A14 14 0 0 1 80 10 L70 20 L74 28 L82 24 A14 14 0 0 1 66 34"/>
      </svg>
      <h2 class="feature-title">BUILD-TO-SUIT OPTIONS</h2>
      <p class="feature-text">Opportunities to create the perfect space.</p>
    </li>
  </ul>

  <div class="abs leasing-band"></div>
  <div class="abs phone-badge">
    <svg width="100" height="100" viewBox="0 0 100 100">
      <path fill="#b87f00" d="M34 28 C30 28 26 32 27 38 C30 54 46 70 62 73 C68 74 72 70 72 66 L72 61 L61 56 L55 62 C47 58 42 53 38 45 L44 39 L39 28 Z"/>
    </svg>
  </div>
  <div class="abs now-leasing">NOW LEASING</div>
  <div class="abs band-divider"></div>
  <div class="abs contact">
    <div class="contact-label">CALL OR TEXT</div>
    <div class="contact-phone">913-555-0186</div>
    <div class="contact-email">jordan@halvernestates.com</div>
  </div>

  <div class="abs brand-dot brand-foot-dot"></div>
  <div class="abs brand-name brand-foot-name">Halvern Estates</div>
</main>
</body>
</html>
```